Hi please see the attached newpaper pages (current) and the new layout in (publisher file). This is a new section in a local newspaper that is going to be branded as trevik.com.au (refer to our site for style etc. - and I've attached out logo. Note - it can be used in reverse as white on blue). This section is currently called "local focus".
I have also attached a copy of one of our vouchers which will go in the top right of the newspaper section. We have allowed room for 8 of these. However, since mocking it up I have also realised we need a space for our own editorial (probably to the left of the vouchers - approx 2 columns wide - note : there are 7 vertical columns to a page on this newspaper). This editorial section should be up to 5 small business tips telling people to go to trevik for more info (so just a brief intro on each tip)
Tip : Keep it clean & simple. Don't over design it.

```html
<!DOCTYPE html>
<html lang="en">
<head>
<meta charset="utf-8">
<title>trevik Business Directory – Newspaper Section</title>
<link rel="stylesheet" href="https://fonts.googleapis.com/css2?family=Arimo:wght@400;700&family=Courier+Prime:wght@700&display=swap">
<style>
  :root {
    --brand-blue: #2295c8;
    --ink: #1e1e1e;
    --ink-soft: #4a4a4a;
    --ad-grey: #e6e6e6;
    --voucher-bg: #f3f7f9;
    --voucher-line: #9fc4d6;
    --paper: #ffffff;
  }
  * { box-sizing: border-box; margin: 0; padding: 0; }
  html, body { width: 1200px; height: 788px; overflow: hidden; background: var(--paper); }
  body { position: relative; font-family: "Arimo", Arial, sans-serif; color: var(--ink); }

  .abs { position: absolute; }

  /* Masthead */
  .brand-name { font-weight: 700; font-size: 46px; line-height: 1; color: var(--brand-blue); letter-spacing: -1px; }
  .brand-url { font-size: 10px; color: var(--ink-soft); letter-spacing: 0.5px; }
  .directory-title { font-size: 17px; font-weight: 700; color: var(--ink-soft); letter-spacing: 0.4px; }
  .directory-tagline { font-size: 16px; font-weight: 700; color: var(--brand-blue); letter-spacing: 0.4px; text-align: right; }
  .swoosh { fill: var(--brand-blue); }

  /* Section bars */
  .section-bar { background: var(--brand-blue); color: #fff; font-size: 16px; font-weight: 700; letter-spacing: 0.6px; padding: 7px 19px; height: 32px; }

  /* Feature copy */
  .feature-col p, .tips-intro { font-size: 10.6px; line-height: 13.4px; color: var(--ink); margin-bottom: 13px; }

  /* Tips */
  .tips-list { list-style: none; }
  .tips-list li { position: relative; padding-left: 16px; font-size: 10.6px; line-height: 13.4px; margin-bottom: 10px; }
  .tips-list li::before { content: ""; position: absolute; left: 3px; top: 3px; width: 8px; height: 8px; border-radius: 50%; background: var(--brand-blue); }

  /* Ads */
  .ad-slot { background: var(--ad-grey); display: flex; align-items: center; justify-content: center; font-size: 29px; color: var(--ink); }

  /* Local deals */
  .deals-title { font-size: 18px; font-weight: 700; color: #3a3a3a; line-height: 0.95; text-align: center; }
  .deals-title strong { font-size: 25px; display: block; }
  .deals-offer { font-size: 15px; font-weight: 700; color: #3a3a3a; text-align: center; line-height: 1.15; }
  .deals-offer span, .deals-note span { color: var(--brand-blue); }
  .deals-note { font-size: 11.5px; font-weight: 700; color: #3a3a3a; text-align: center; line-height: 1.15; }

  .voucher-grid { display: grid; grid-template-columns: 1fr 1fr; grid-template-rows: repeat(4, 1fr); gap: 1px; background: var(--voucher-line); border: 1px solid var(--voucher-line); }
  .voucher { background: var(--voucher-bg); padding: 3px 3px 2px; position: relative; overflow: hidden; }
  .voucher-head { display: flex; justify-content: space-between; align-items: flex-start; height: 24px; }
  .voucher-brand { font-size: 13px; font-weight: 700; color: var(--brand-blue); line-height: 1; }
  .voucher-brand small { display: block; font-size: 3.5px; font-weight: 400; color: var(--ink-soft); }
  .voucher-badge { border: 1px solid #8aa; background: #fff; font-family: "Courier Prime", "Courier New", monospace; font-weight: 700; font-size: 12px; padding: 3px 4px; line-height: 1; }
  .voucher-name { font-size: 7px; font-weight: 700; text-align: center; margin-top: 1px; }
  .voucher-fine { font-size: 3.6px; text-align: center; color: var(--ink-soft); line-height: 5px; }
  .voucher-offer { font-size: 6px; text-align: center; line-height: 7px; margin-top: 2px; }
  .voucher-foot { display: flex; justify-content: space-between; font-size: 3.6px; color: var(--ink-soft); position: absolute; left: 3px; right: 3px; bottom: 2px; }
</style>
</head>
<body>

<!-- Left page -->
<div class="abs brand-name" style="left:30px;top:26px;">trevik</div>
<div class="abs brand-url" style="left:34px;top:72px;">www.trevik.com.au</div>
<div class="abs directory-title" style="left:163px;top:28px;">trevik Business Directory</div>
<div class="abs directory-tagline" style="left:242px;top:47px;width:300px;">Supporting local W.A businesses</div>
<svg class="abs" style="left:150px;top:72px;" width="392" height="16" viewBox="0 0 392 16" aria-hidden="true"><path class="swoosh" d="M0 16 Q50 1 130 0 H392 V16 Z"/></svg>

<div class="abs section-bar" style="left:15px;top:94px;width:527px;">Local Business Feature</div>

<div class="abs feature-col" style="left:47px;top:144px;width:205px;">
  <p>"Lorem ipsum dolor sit amet, consecte-tur adipisicing elit, sed do eiusmod tempor incididunt ut labore et dolore magna aliqua. Ut enim ad minim veniam, quis nostrud exercitation ullamco laboris nisi ut aliquip ex ea commodo conse-quat. Duis aute irure dolor in reprehen-derit in voluptate velit esse cillum dolore eu fugiat nulla pariatur. Excepteur sint occaecat cupidatat non proident, sunt in culpa qui officia deserunt mollit anim id est laborum."</p>
  <p>"Lorem ipsum dolor sit amet, consecte-tur adipisicing elit, sed do eiusmod tempor incididunt ut labore et dolore magna aliqua. Ut enim ad minim veniam, quis nostrud exercitation ullamco laboris nisi ut aliquip ex ea commodo conse-quat. Duis aute irure dolor in reprehen-derit in voluptate velit esse cillum dolore eu fugiat nulla pariatur. Excepteur sint occaecat cupidatat non proident, sunt in culpa qui officia deserunt mollit anim id est laborum."</p>
</div>
<div class="abs feature-col" style="left:283px;top:144px;width:210px;">
  <p>"Lorem ipsum dolor sit amet, consecte-tur adipisicing elit, sed do eiusmod tempor incididunt ut labore et dolore magna aliqua. Ut enim ad minim veniam, quis nostrud exercitation ullamco laboris nisi ut aliquip ex ea commodo conse-quat. Duis aute irure dolor in reprehen-derit in voluptate velit esse cillum dolore eu fugiat nulla pariatur. Excepteur sint occaecat cupidatat non proident, sunt in culpa qui officia deserunt mollit anim id est laborum."</p>
  <p>"Lorem ipsum dolor sit amet, consecte-tur adipisicing elit, sed do eiusmod tempor incididunt ut labore et dolore magna aliqua. Ut enim ad minim veniam, quis nostrud exercitation ullamco laboris nisi ut aliquip ex ea commodo conse-quat. Duis aute irure dolor in reprehen-derit in voluptate velit esse cillum dolore eu fugiat nulla pariatur. Excepteur sint occaecat cupidatat non proident, sunt in culpa qui officia deserunt mollit anim id est laborum."</p>
</div>

<div class="abs ad-slot" style="left:15px;top:512px;width:260px;height:128px;">Ads</div>
<div class="abs ad-slot" style="left:283px;top:512px;width:259px;height:128px;">Ads</div>
<div class="abs ad-slot" style="left:15px;top:648px;width:260px;height:128px;">Ads</div>
<div class="abs ad-slot" style="left:283px;top:648px;width:259px;height:128px;">Ads</div>

<!-- Right page -->
<div class="abs brand-name" style="left:576px;top:26px;">trevik</div>
<div class="abs brand-url" style="left:580px;top:72px;">www.trevik.com.au</div>
<div class="abs directory-title" style="left:724px;top:28px;">trevik Business Directory</div>
<div class="abs directory-tagline" style="left:700px;top:51px;width:238px;">Stay True to trevik</div>
<svg class="abs" style="left:700px;top:72px;" width="245" height="16" viewBox="0 0 245 16" aria-hidden="true"><path class="swoosh" d="M0 16 Q40 1 100 0 H245 V16 Z"/></svg>

<div class="abs ad-slot" style="left:566px;top:94px;width:137px;height:400px;">Ads</div>

<div class="abs section-bar" style="left:711px;top:94px;width:234px;">trevik Business Tips</div>
<div class="abs" style="left:724px;top:144px;width:212px;">
  <p class="tips-intro">"Lorem ipsum dolor sit amet, consecte-tur adipisicing elit, sed do eiusmod tempor incididunt ut labore et dolore magna aliqua.</p>
  <ul class="tips-list">
    <li>Ut enim ad minim veniam, quis nos-trud exercitation ullamco laboris nisi ut aliquip ex ea commodo consequat.</li>
    <li>Duis aute irure dolor in reprehenderit in voluptate velit esse cillum dolore eu fugiat nulla pariatur.</li>
    <li>Excepteur sint occaecat cupidatat non proident, sunt in culpa qui officia de-serunt mollit anim id est laborum."</li>
    <li>"Lorem ipsum dolor sit amet, con-sectetur adipisicing elit, sed do eius-mod tempor incididunt ut labore et dolore magna aliqua.</li>
    <li>Ut enim ad minim veniam, quis nos-trud exercitation ullamco laboris nisi ut aliquip ex ea commodo consequat. cia deserunt mollit anim id est labo-rum.</li>
  </ul>
</div>

<div class="abs deals-title" style="left:962px;top:27px;width:76px;">LOCAL<strong>DEALS</strong></div>
<div class="abs deals-offer" style="left:1050px;top:30px;width:125px;">Add one <span>FREE</span><br>to your business</div>
<div class="abs" style="left:954px;top:72px;width:229px;height:14px;background:var(--brand-blue);"></div>

<div class="abs voucher-grid" style="left:954px;top:92px;width:229px;height:342px;">
  <div class="voucher"><div class="voucher-head"><div class="voucher-brand">trevik<small>trevik.com.au</small></div><div class="voucher-badge">50% OFF</div></div><div class="voucher-name">Steady Ride Rider School</div><div class="voucher-fine">Lakeside WA<br>Phone: 0400 000 000</div><div class="voucher-offer">FIRST LESSON HALF PRICE !<br>THAT'S JUST $35 p/hr.</div><div class="voucher-fine">Valid for one first lesson per new rider</div><div class="voucher-foot"><span>hello@steadyride.com.au</span><span>Valid until 30 Dec 2025</span></div></div>
  <div class="voucher"><div class="voucher-head"><div class="voucher-brand">trevik<small>trevik.com.au</small></div><div class="voucher-badge">50% OFF</div></div><div class="voucher-name">Steady Ride Rider School</div><div class="voucher-fine">Lakeside WA<br>Phone: 0400 000 000</div><div class="voucher-offer">FIRST LESSON HALF PRICE !<br>THAT'S JUST $35 p/hr.</div><div class="voucher-fine">Valid for one first lesson per new rider</div><div class="voucher-foot"><span>hello@steadyride.com.au</span><span>Valid until 30 Dec 2025</span></div></div>
  <div class="voucher"><div class="voucher-head"><div class="voucher-brand">trevik<small>trevik.com.au</small></div><div class="voucher-badge">50% OFF</div></div><div class="voucher-name">Steady Ride Rider School</div><div class="voucher-fine">Lakeside WA<br>Phone: 0400 000 000</div><div class="voucher-offer">FIRST LESSON HALF PRICE !<br>THAT'S JUST $35 p/hr.</div><div class="voucher-fine">Valid for one first lesson per new rider</div><div class="voucher-foot"><span>hello@steadyride.com.au</span><span>Valid until 30 Dec 2025</span></div></div>
  <div class="voucher"><div class="voucher-head"><div class="voucher-brand">trevik<small>trevik.com.au</small></div><div class="voucher-badge">50% OFF</div></div><div class="voucher-name">Steady Ride Rider School</div><div class="voucher-fine">Lakeside WA<br>Phone: 0400 000 000</div><div class="voucher-offer">FIRST LESSON HALF PRICE !<br>THAT'S JUST $35 p/hr.</div><div class="voucher-fine">Valid for one first lesson per new rider</div><div class="voucher-foot"><span>hello@steadyride.com.au</span><span>Valid until 30 Dec 2025</span></div></div>
  <div class="voucher"><div class="voucher-head"><div class="voucher-brand">trevik<small>trevik.com.au</small></div><div class="voucher-badge">50% OFF</div></div><div class="voucher-name">Steady Ride Rider School</div><div class="voucher-fine">Lakeside WA<br>Phone: 0400 000 000</div><div class="voucher-offer">FIRST LESSON HALF PRICE !<br>THAT'S JUST $35 p/hr.</div><div class="voucher-fine">Valid for one first lesson per new rider</div><div class="voucher-foot"><span>hello@steadyride.com.au</span><span>Valid until 30 Dec 2025</span></div></div>
  <div class="voucher"><div class="voucher-head"><div class="voucher-brand">trevik<small>trevik.com.au</small></div><div class="voucher-badge">50% OFF</div></div><div class="voucher-name">Steady Ride Rider School</div><div class="voucher-fine">Lakeside WA<br>Phone: 0400 000 000</div><div class="voucher-offer">FIRST LESSON HALF PRICE !<br>THAT'S JUST $35 p/hr.</div><div class="voucher-fine">Valid for one first lesson per new rider</div><div class="voucher-foot"><span>hello@steadyride.com.au</span><span>Valid until 30 Dec 2025</span></div></div>
  <div class="voucher"><div class="voucher-head"><div class="voucher-brand">trevik<small>trevik.com.au</small></div><div class="voucher-badge">50% OFF</div></div><div class="voucher-name">Steady Ride Rider School</div><div class="voucher-fine">Lakeside WA<br>Phone: 0400 000 000</div><div class="voucher-offer">FIRST LESSON HALF PRICE !<br>THAT'S JUST $35 p/hr.</div><div class="voucher-fine">Valid for one first lesson per new rider</div><div class="voucher-foot"><span>hello@steadyride.com.au</span><span>Valid until 30 Dec 2025</span></div></div>
  <div class="voucher"><div class="voucher-head"><div class="voucher-brand">trevik<small>trevik.com.au</small></div><div class="voucher-badge">50% OFF</div></div><div class="voucher-name">Steady Ride Rider School</div><div class="voucher-fine">Lakeside WA<br>Phone: 0400 000 000</div><div class="voucher-offer">FIRST LESSON HALF PRICE !<br>THAT'S JUST $35 p/hr.</div><div class="voucher-fine">Valid for one first lesson per new rider</div><div class="voucher-foot"><span>hello@steadyride.com.au</span><span>Valid until 30 Dec 2025</span></div></div>
</div>

<div class="abs deals-note" style="left:954px;top:445px;width:229px;">Add a deal to your Business <span>FREE</span><br>visit <span>www.trevik.com.au</span> &amp; go to<br>“add your business-free at the<br>top ofthe home page</div>

<div class="abs ad-slot" style="left:566px;top:512px;width:182px;height:188px;">Ads</div>
<div class="abs ad-slot" style="left:754px;top:512px;width:181px;height:188px;">Ads</div>
<div class="abs ad-slot" style="left:566px;top:708px;width:369px;height:68px;">Ads</div>
<div class="abs ad-slot" style="left:954px;top:512px;width:229px;height:264px;">Ads</div>

</body>
</html>
```